A webite for an Urgent Care for children

We need a design for a new website for an Urgent care for kids. We are based in Atlanta, GA and provide quality after-hours and urgent care services for children. We will appreciate an innovative design that employs flash technology, especially on the Home page. We also want there to be a Contact Us form. There should also be a control panel with the ability for us to make quick and minor edits on the website as needed without requiring the services of an expert.

Target Market(s)

Parents, children, general audience

Industry/Entity Type

Healthcare

Coding

Coded - Design and coding required

Number of Pages Required

5+ page

Font styles to use
Sans Serif
Decorative

Colors
acd037
acd136
cadf82
eaf2ce
f6faec

Requirements
Must have
• Mobile devices website capable
• Link to social media, Facebook, twitter, etc
Nice to have
• Ability for customers to pay online.

```html
<!DOCTYPE html>
<html lang="en">
<head>
<meta charset="utf-8">
<title>Little Harbor Urgent Care</title>
<link href="https://fonts.googleapis.com/css2?family=Raleway:wght@400;500;600;700;800&display=swap" rel="stylesheet">
<style>
:root{
  --green:#acd037;
  --green-2:#acd136;
  --green-soft:#cadf82;
  --green-pale:#eaf2ce;
  --green-mist:#f6faec;
  --red:#d9302b;
  --pink:#e2618a;
  --blue:#3ea6ea;
  --ink:#3b3b3b;
  --text:#555;
  --dark:#333;
}
*{box-sizing:border-box;margin:0;padding:0}
html,body{width:774px;height:1200px;overflow:hidden}
body{font-family:'Raleway',sans-serif;color:var(--text);position:relative;
  background:linear-gradient(180deg,var(--green-soft) 0,var(--green-pale) 420px,var(--green-mist) 900px,var(--green-mist) 100%)}
.abs{position:absolute}
.page-card{left:38px;top:58px;width:696px;height:1040px;background:#fff;border-radius:8px 8px 0 0}
.logo-bump{left:250px;top:10px;width:275px;height:110px;background:#fff;border-radius:50% 50% 0 0/100% 100% 0 0}
.logo{left:250px;top:30px;width:275px;text-align:center;font-weight:800;font-size:21px;line-height:26px;color:#2f6fc0;letter-spacing:.5px}
.follow{left:49px;top:64px;display:flex;align-items:center;gap:4px;font-size:10px;font-weight:700;color:var(--red)}
.follow .dot{width:20px;height:20px;border-radius:50%}
.call{right:48px;top:66px;font-size:10px;font-weight:700;color:var(--red);display:flex;align-items:center;gap:5px}
.nav{left:48px;top:89px;width:678px;height:32px;background:var(--green);border-radius:8px 8px 0 0;display:flex;justify-content:space-around;align-items:center;padding:0 10px}
.nav a{color:#fff;font-size:9.5px;font-weight:700;text-decoration:none;letter-spacing:.2px}
.hero{left:48px;top:121px;width:678px;height:303px;border-radius:0 0 8px 8px;overflow:hidden;
  background:linear-gradient(90deg,#e9cbd6 0,#dcb0c4 35%,#c98fa6 60%,#b2778a 100%)}
.hero-title{left:65px;top:212px;font-size:24px;font-weight:700;color:var(--red);letter-spacing:.3px}
.hero-text{left:66px;top:244px;width:280px;font-size:12.5px;line-height:17.5px;color:#333;font-weight:500}
.hero-btn{left:66px;top:311px;width:275px;height:31px;background:var(--green);color:#fff;font-size:10px;font-weight:700;display:flex;align-items:center;justify-content:center}
.dots{left:69px;top:388px;display:flex;gap:5px}
.dots i{width:6px;height:6px;border-radius:50%;background:#fff}
.dots i:first-child{background:#111}
.feature{top:457px;width:213px;height:220px}
.feature .photo{height:124px}
.feature .cap{height:96px;border-radius:0 0 50% 50%/0 0 100% 100%;color:#fff;font-size:13.5px;font-weight:700;text-align:center;padding-top:22px;line-height:18px;letter-spacing:.3px}
.welcome{left:48px;top:712px;width:446px;height:364px;background:var(--green-pale);border-radius:8px;padding:22px 19px 0}
.welcome h2{width:205px;font-size:14px;line-height:18px;font-weight:700;color:var(--ink);letter-spacing:.4px;margin-bottom:9px}
.welcome p{font-size:9.3px;line-height:15px;margin-bottom:4px;color:#555}
.welcome .narrow{width:205px}
.welcome-photo{left:280px;top:740px;width:200px;height:124px;border-radius:8px;background:linear-gradient(135deg,#8fb3d6,#c7d7e8 50%,#e7a4a4)}
.welcome .walk{color:var(--green);font-weight:700;font-size:9.5px;margin-top:9px}
.contact{left:512px;top:712px;width:214px;height:364px;background:var(--green-soft);border-radius:8px;padding:18px 15px 0}
.contact h2{font-size:15px;font-weight:700;color:var(--ink);letter-spacing:.5px;margin-bottom:11px}
.field{height:26px;background:#fff;font-size:9px;color:#444;padding:0 11px;display:flex;align-items:center;justify-content:space-between;margin-bottom:9px}
.field.msg{height:94px;align-items:flex-start;padding-top:9px}
.submit{left:630px;top:1038px;width:80px;height:25px;background:var(--dark);color:#fff;font-size:11px;font-weight:700;display:flex;align-items:center;justify-content:center}
.footer{left:0;top:1087px;width:774px;height:113px;background:var(--green)}
.foot-links{left:48px;top:1114px;font-size:9px;color:#fff;word-spacing:1px}
.foot-copy{left:48px;top:1147px;font-size:8.5px;color:#fff;line-height:16px}
.foot-contact{left:552px;top:1102px;font-size:9px;color:#fff;line-height:14.5px}
.foot-contact h3{font-size:9.5px;font-weight:700;margin-bottom:2px}
.foot-contact .body{padding-left:4px}
</style>
</head>
<body>
<div class="abs page-card"></div>
<div class="abs logo-bump"></div>
<div class="abs logo">Little Harbor<br>Urgent Care</div>

<div class="abs follow">FOLLOW US&nbsp;<span class="dot" style="background:#3b5998"></span><span class="dot" style="background:#1da1f2"></span></div>
<div class="abs call">
  <svg width="9" height="9" viewBox="0 0 24 24"><path fill="currentColor" d="M6.6 10.8a15 15 0 0 0 6.6 6.6l2.2-2.2c.3-.3.7-.4 1-.2 1.1.4 2.3.6 3.6.6.6 0 1 .4 1 1V20c0 .6-.4 1-1 1A17 17 0 0 1 3 4c0-.6.4-1 1-1h3.5c.6 0 1 .4 1 1 0 1.3.2 2.5.6 3.6.1.3 0 .7-.2 1z"/></svg>
  CALL US: (555) 014-2900</div>

<nav class="abs nav">
  <a>HOME</a><a>ABOUT US</a><a>OUR SERVICES</a><a>FINANCE AND INSURANCE</a><a>OFFICE FORMS</a><a>CONTACT US</a><a>FAQ</a>
</nav>

<div class="abs hero" role="img" aria-label="Smiling pediatric nurse holding a happy toddler"></div>
<div class="abs hero-title">LITTLE HARBOR URGENT CARE</div>
<div class="abs hero-text">We are based in Atlanta, Georgia and provide quality after-hours and urgent care services for children.</div>
<div class="abs hero-btn">IF YOU HAVE AN EMERGENCY, PLEASE DIAL 911</div>
<div class="abs dots"><i></i><i></i><i></i><i></i></div>

<div class="abs feature" style="left:48px">
  <div class="photo" role="img" aria-label="Little girl playing doctor with a doll in a playroom" style="background:linear-gradient(135deg,#9fcf6a,#e9dfd2 55%,#e98bb2)"></div>
  <div class="cap" style="background:var(--green)">FAN &amp; PLAYFUL<br>OFFICE</div>
</div>
<div class="abs feature" style="left:281px">
  <div class="photo" role="img" aria-label="Nurse listening to a toddler with a stethoscope" style="background:linear-gradient(135deg,#d8d8d8,#f1ede6 50%,#c9b7a3)"></div>
  <div class="cap" style="background:var(--pink)">URGENT CARE FOR<br>CHILDREN</div>
</div>
<div class="abs feature" style="left:513px">
  <div class="photo" role="img" aria-label="Mother and daughter greeting a doctor" style="background:linear-gradient(135deg,#e6b8c7,#efe6e4 50%,#c9d3e2)"></div>
  <div class="cap" style="background:var(--blue)">QUALITY AFTER<br>HOURS</div>
</div>

<section class="abs welcome">
  <h2>WELCOME TO<br>LITTLE HARBOR</h2>
  <p class="narrow">Welcome to Little Harbor Urgent Care, your after-hours pediatric urgent care.</p>
  <p class="narrow">We are here when your little ones suddenly wake up sick or sustain an injury and you need immediate medical attention, but your regular doctor's office is closed.</p>
  <p style="margin-top:8px">We are unique in the services we provide and are an alternative when your child needs care after-hours to be treated by pediatricians who specialize in caring for children.</p>
  <p>We are available so you do not have to take your child to a crowded Emergency Room to be treated by providers who are not pediatricians and do not specialize in caring for children. And also save you from the high cost of an ER visit.</p>
  <p>Our services are quick and our medical professionals are ready to serve you in our clean, friendly and professional environment.</p>
  <p>We are open every day, late into the night and weekends.</p>
  <p>Cash-pay is welcome. We also accept most insurances and credit cards.</p>
  <p class="walk">Walk-ins welcome.</p>
</section>
<div class="abs welcome-photo" role="img" aria-label="Nurse with a young girl holding a teddy bear"></div>

<section class="abs contact">
  <h2>QUICK CONTACT</h2>
  <div class="field">Name</div>
  <div class="field">Email Address</div>
  <div class="field">Phone Number</div>
  <div class="field">Inquiry <svg width="7" height="5" viewBox="0 0 10 6"><path d="M1 1l4 4 4-4" stroke="#444" fill="none" stroke-width="1.5"/></svg></div>
  <div class="field">Subject</div>
  <div class="field msg">Message</div>
</section>
<div class="abs submit">Submit</div>

<footer class="abs footer"></footer>
<div class="abs foot-links">Home&nbsp; /&nbsp; About Us&nbsp; /&nbsp; Our Services&nbsp; /&nbsp; Finance and Insurance&nbsp; /&nbsp; Office Forms&nbsp; /&nbsp; Contact Us&nbsp; /&nbsp; FAQ</div>
<div class="abs foot-copy">Copyright © 2016. Comapny Name. All Right Reserved<br>Disclaimer / Terms and Conditions</div>
<div class="abs foot-contact">
  <h3>CONTAT DETAILS</h3>
  <div class="body">
    <strong>Little Harbor Urgent Care</strong><br>
    22 Maple Court Riverbend<br>
    GA 30299<br>
    <svg width="8" height="8" viewBox="0 0 24 24"><path fill="#fff" d="M6.6 10.8a15 15 0 0 0 6.6 6.6l2.2-2.2c.3-.3.7-.4 1-.2 1.1.4 2.3.6 3.6.6.6 0 1 .4 1 1V20c0 .6-.4 1-1 1A17 17 0 0 1 3 4c0-.6.4-1 1-1h3.5c.6 0 1 .4 1 1 0 1.3.2 2.5.6 3.6.1.3 0 .7-.2 1z"/></svg>
    (555) 014-2900 &nbsp;|&nbsp;
    <svg width="8" height="8" viewBox="0 0 24 24"><rect x="3" y="8" width="18" height="12" rx="2" fill="#fff"/><rect x="7" y="3" width="10" height="6" fill="#fff"/></svg>
    (555) 014-2901
  </div>
</div>
</body>
</html>
```